Design Challege - Simplify a Complex Message

We have a new website design, but one of the pages presents a particular problem.

Our company does ERP implementations. We have developed a proprietary approach to these implementations based on the idea that you must get eight (and only eight) things right. These eight things are listed below, summarized in one or two words each:

1. Value
2. Capability
3. Functionality
4. Data
5. Technology
6. Change Leadership
7. Quality
8. Governance

Each of these eight things can be summarized in a short paragraph, but when you combine all eight summaries with a brief introductory text, the result is a lot of text - so much text that the casual surfer may be overwhelmed by it.

The winning design will find an engaging way to present the information in a way that presents a high-level summary, using icons and one- or two-word descriptions above but revealing more information when clicked.

Our current design for this information, with a paragraph describing the eight elements in a table, is included as an upload in PDF and Microsoft Word formats. We are looking for a creative way to display these eight things, showing the detail only when the user wants to see it.

The website is being built in WordPress, using Elementor as a page builder.

We will implement (code) the page, but the winner will be asked to specify the widget or other add-in if one is required.

The design does not need to include a header or footer, we have those.

Target Market(s)

Business executives working in technology

Industry/Entity Type

Any

Number of Pages Required

1 page

Font styles to use
Sans Serif

Requirements
Must have
• A design for the body of the page, but not the header or footer.
Nice to have
• Unique icons or images appropriate for each of the eight things.
Should not have
• A lot of text on one page

```html
<!DOCTYPE html>
<html lang="en">
<head>
<meta charset="UTF-8">
<title>ERP Implementations – 8 Things to Get Right</title>
<link href="https://fonts.googleapis.com/css2?family=Poppins:wght@400;500;600;700&display=swap" rel="stylesheet">
<style>
  :root {
    --page-bg: #f5f4fc;
    --card-bg: #f5f4fc;
    --open-bg: #ffffff;
    --border: #cfd3df;
    --brand: #2a6496;
    --brand-dark: #24557f;
    --heading: #1f1f1f;
    --text: #4a4a4a;
    --muted: #9a9a9a;
    --chevron: #4a4a4a;
  }
  * { box-sizing: border-box; margin: 0; padding: 0; }
  html, body {
    width: 1200px; height: 1159px; overflow: hidden;
    background: var(--page-bg);
    font-family: "Poppins", sans-serif;
    color: var(--text);
  }
  .page { position: relative; width: 1200px; height: 1159px; }

  .option-switch { position: absolute; top: 24px; right: 26px; display: flex; gap: 8px; }
  .option-switch span {
    height: 22px; padding: 0 10px; border-radius: 11px;
    font-size: 10.5px; line-height: 22px; color: var(--muted); background: #fff;
  }
  .option-switch .is-active { background: var(--brand); color: #fff; font-weight: 500; }

  .intro { position: absolute; left: 278px; top: 86px; width: 650px; }
  .eyebrow { font-size: 17.5px; color: var(--brand); font-weight: 400; line-height: 24px; }
  .title { font-size: 29px; font-weight: 600; color: var(--heading); line-height: 40px; margin-top: 3px; }
  .intro p { font-size: 11.8px; line-height: 20px; margin-top: 40px; }
  .intro p + p { margin-top: 20px; }
  .intro strong { font-weight: 600; color: #333; }
  .hint { display: flex; align-items: center; gap: 5px; margin-top: 20px; font-size: 11.8px; font-weight: 600; color: #3a3a3a; }
  .hint svg { width: 21px; height: 21px; }

  .accordion { position: absolute; left: 271px; top: 382px; width: 664px; }
  .acc-item {
    border: 1px solid var(--border); border-radius: 5px;
    background: var(--card-bg); margin-bottom: 8px;
  }
  .acc-head {
    height: 48px; display: flex; align-items: center; justify-content: space-between;
    padding: 0 10px 0 10px; font-size: 17.5px; font-weight: 500; color: #3d3d3d;
  }
  .acc-head svg { width: 14px; height: 14px; }
  .acc-item.is-open { background: var(--open-bg); box-shadow: 0 2px 4px rgba(0,0,0,.12); margin-top: 12px; }
  .acc-item.is-open .acc-head { border-bottom: 1px solid var(--border); }
  .acc-body { position: relative; height: 203px; padding: 19px 30px 0 81px; }
  .acc-icon { position: absolute; left: 24px; top: 8px; width: 48px; height: 60px; }
  .acc-body p { font-size: 11.8px; line-height: 20px; }
  .acc-body ul { list-style: none; margin: 20px 0 0 12px; }
  .acc-body li { font-size: 11.8px; line-height: 20px; position: relative; padding-left: 9px; }
  .acc-body li::before { content: "•"; position: absolute; left: -3px; font-size: 9px; }
  .learn-more { display: inline-flex; align-items: center; gap: 8px; margin-top: 15px; font-size: 11.5px; font-weight: 500; color: var(--brand); text-decoration: none; }
  .learn-more svg { width: 12px; height: 12px; }
</style>
</head>
<body>
<main class="page">
  <nav class="option-switch">
    <span>Option 1</span><span>Option 2</span><span class="is-active">Option 3</span>
  </nav>

  <section class="intro">
    <div class="eyebrow">ERP Implementations</div>
    <h1 class="title">8 Things to Get Right</h1>
    <p>Like the roots and branches of a tree, there are many considerations in an ERP implementation. Focus too much on the minor details, and you can lose sight of the tree.</p>
    <p>In an ERP implementation, you must get <strong>eight major things</strong> right to be successful. Ignore any of them, and your implementation will fail. Get them right, and you will likely succeed.</p>
    <div class="hint">
      <svg viewBox="0 0 24 24"><circle cx="12" cy="12" r="12" fill="#4a4a4a"/><circle cx="13.3" cy="6.5" r="1.6" fill="#fff"/><path d="M12.2 10h2l-2 8.5h-2z" fill="#fff"/></svg>
      Click the points below to read its description.
    </div>
  </section>

  <section class="accordion">
    <div class="acc-item"><div class="acc-head">1. Value<svg viewBox="0 0 14 14"><path d="M2 4.5l5 5 5-5" fill="none" stroke="var(--chevron)" stroke-width="2.2"/></svg></div></div>

    <div class="acc-item is-open">
      <div class="acc-head">2. Capability<svg viewBox="0 0 14 14"><path d="M4.5 2l5 5-5 5" fill="none" stroke="var(--chevron)" stroke-width="2.2"/></svg></div>
      <div class="acc-body">
        <svg class="acc-icon" viewBox="0 0 48 60" aria-hidden="true">
          <g fill="var(--brand)">
            <path d="M22 9c-9 0-15 6-15 14 0 5 3 8 5 11 1.5 2 2 4 2 6h8z"/>
            <path d="M25 9c8 0 13 6 13 13 0 5-3 8-5 11-1.5 2-2 4-2 7h-6z" opacity=".85"/>
            <rect x="13" y="43" width="20" height="3" rx="1.5"/>
            <rect x="13" y="48" width="20" height="3" rx="1.5"/>
            <rect x="16" y="53" width="14" height="3" rx="1.5"/>
          </g>
          <g stroke="var(--brand)" stroke-width="1.6" stroke-linecap="round">
            <path d="M23 0v5"/><path d="M41 8l-4 4"/><path d="M47 25h-5"/><path d="M41 41l-4-4"/>
          </g>
        </svg>
        <p>The company and the implementation team must be capable of implementing the project on their own or with help. The project must have the following:</p>
        <ul>
          <li>Resources required, including people, time, and budget.</li>
          <li>Processes required, usually delivered through a comprehensive methodology.</li>
          <li>Prioritization required because an ERP project will need the commitment of the entire company.</li>
        </ul>
        <a class="learn-more" href="#">Learn More<svg viewBox="0 0 12 12"><path d="M1 6h9M6.5 2.5L10 6l-3.5 3.5" fill="none" stroke="var(--brand)" stroke-width="1.6"/></svg></a>
      </div>
    </div>

    <div class="acc-item"><div class="acc-head">3. Functionality<svg viewBox="0 0 14 14"><path d="M2 4.5l5 5 5-5" fill="none" stroke="var(--chevron)" stroke-width="2.2"/></svg></div></div>
    <div class="acc-item"><div class="acc-head">4. Data<svg viewBox="0 0 14 14"><path d="M2 4.5l5 5 5-5" fill="none" stroke="var(--chevron)" stroke-width="2.2"/></svg></div></div>
    <div class="acc-item"><div class="acc-head">5. Technology<svg viewBox="0 0 14 14"><path d="M2 4.5l5 5 5-5" fill="none" stroke="var(--chevron)" stroke-width="2.2"/></svg></div></div>
    <div class="acc-item"><div class="acc-head">6. Change Leadership<svg viewBox="0 0 14 14"><path d="M2 4.5l5 5 5-5" fill="none" stroke="var(--chevron)" stroke-width="2.2"/></svg></div></div>
    <div class="acc-item"><div class="acc-head">7. Quality<svg viewBox="0 0 14 14"><path d="M2 4.5l5 5 5-5" fill="none" stroke="var(--chevron)" stroke-width="2.2"/></svg></div></div>
    <div class="acc-item"><div class="acc-head">8. Governance<svg viewBox="0 0 14 14"><path d="M2 4.5l5 5 5-5" fill="none" stroke="var(--chevron)" stroke-width="2.2"/></svg></div></div>
  </section>
</main>
</body>
</html>
```